Road Construction Company needs business cards

We would like a new business card designed for our business.

We're a road construction company based in Qld, Australia.

Can the business card please have the following information on it.

Name: Brent Malvoy
Position: General Manager
Phone: 0471 592 304
Email: Brent.malvoy@quendix.com.au
Address: 87 Harrowgate Ave, Pindarra, QLD, 4000
Website: www.quendix.com.au

Visually we'd like the card to be professional and simple.

Attached is our logo.

Our website is www.quendix.com.au

Target Market(s)

Men aged 25-60

Contact Information for Business Card

As listed in project description

Font styles to use
Serif

Requirements
Must have
• Large logo on back of card

```html
<!DOCTYPE html>
<html lang="en">
<head>
<meta charset="utf-8">
<title>Quendix Road Construction – Business Card</title>
<link href="https://fonts.googleapis.com/css2?family=Source+Sans+3:wght@400;600;800&display=swap" rel="stylesheet">
<style>
  :root {
    --backdrop: #a8a8a8;
    --card-white: #ffffff;
    --brand-blue: #0a5aa8;
    --back-blue: #0066b3;
    --ice-blue: #cfe9f4;
    --text-font: "Source Sans 3", sans-serif;
  }
  html, body {
    margin: 0;
    padding: 0;
    width: 1200px;
    height: 1200px;
    overflow: hidden;
    background: var(--backdrop);
    font-family: var(--text-font);
  }
  .stage {
    width: 1200px;
    height: 1200px;
    display: flex;
    flex-direction: column;
    align-items: center;
    justify-content: center;
    gap: 60px;
  }
  .card {
    position: relative;
    width: 760px;
    height: 464px;
    border-radius: 30px;
    overflow: hidden;
    box-shadow: 0 14px 30px rgba(0,0,0,0.25);
  }
  .card-front { background: var(--card-white); color: var(--brand-blue); }
  .card-back {
    background: var(--back-blue);
    display: flex;
    align-items: center;
    justify-content: center;
  }
  .corner-peak { position: absolute; left: 0; top: 0; }
  .wordmark {
    position: absolute;
    left: 420px;
    top: 78px;
    margin: 0;
    font-weight: 800;
    font-size: 58px;
    letter-spacing: 1px;
    color: var(--brand-blue);
    line-height: 1;
  }
  .identity {
    position: absolute;
    right: 420px;
    top: 205px;
    text-align: right;
  }
  .person-name {
    margin: 0;
    font-size: 42px;
    font-weight: 400;
    line-height: 1.05;
    white-space: nowrap;
  }
  .person-role {
    margin: 2px 0 0;
    font-size: 27px;
    font-weight: 400;
    white-space: nowrap;
  }
  .divider {
    position: absolute;
    left: 362px;
    top: 210px;
    width: 2px;
    height: 112px;
    background: var(--brand-blue);
  }
  .contact-list {
    position: absolute;
    left: 378px;
    top: 218px;
    margin: 0;
    padding: 0;
    list-style: none;
    font-size: 21px;
  }
  .contact-list li {
    display: flex;
    align-items: center;
    gap: 10px;
    height: 34px;
    white-space: nowrap;
  }
  .contact-list svg { width: 18px; height: 18px; flex: none; }
  .address {
    position: absolute;
    left: 56px;
    bottom: 48px;
    display: flex;
    align-items: center;
    gap: 10px;
    font-size: 22px;
    white-space: nowrap;
  }
  .address svg { width: 18px; height: 24px; }
  .back-wordmark {
    margin: 0;
    font-weight: 800;
    font-size: 120px;
    letter-spacing: 3px;
    color: var(--card-white);
    line-height: 1;
  }
</style>
</head>
<body>
<main class="stage">
  <section class="card card-front" aria-label="Business card front">
    <svg class="corner-peak" width="260" height="260" viewBox="0 0 260 260" aria-hidden="true">
      <polygon points="0,0 45,0 218,190 80,158 0,236" fill="var(--ice-blue)"/>
    </svg>
    <p class="wordmark">QUENDIX</p>
    <div class="identity">
      <h1 class="person-name">Brent Malvoy</h1>
      <p class="person-role">General Manager</p>
    </div>
    <div class="divider"></div>
    <ul class="contact-list">
      <li>
        <svg viewBox="0 0 24 24" aria-hidden="true"><path fill="var(--brand-blue)" d="M6.6 10.8a15.1 15.1 0 0 0 6.6 6.6l2.2-2.2a1 1 0 0 1 1-.25 11.4 11.4 0 0 0 3.6.57 1 1 0 0 1 1 1V20a1 1 0 0 1-1 1A17 17 0 0 1 3 4a1 1 0 0 1 1-1h3.5a1 1 0 0 1 1 1c0 1.25.2 2.45.57 3.57a1 1 0 0 1-.25 1z"/></svg>
        0471 592 304
      </li>
      <li>
        <svg viewBox="0 0 24 24" aria-hidden="true"><rect x="2" y="5" width="20" height="14" rx="1.5" fill="var(--brand-blue)"/><path d="M3 6l9 7 9-7" fill="none" stroke="#fff" stroke-width="1.6"/></svg>
        Brent.malvoy@quendix.com.au
      </li>
      <li>
        <svg viewBox="0 0 24 24" aria-hidden="true"><g fill="none" stroke="var(--brand-blue)" stroke-width="1.6"><circle cx="12" cy="12" r="9.5"/><ellipse cx="12" cy="12" rx="4" ry="9.5"/><path d="M2.5 12h19M4 7h16M4 17h16"/></g></svg>
        www.quendix.com.au
      </li>
    </ul>
    <p class="address">
      <svg viewBox="0 0 18 24" aria-hidden="true"><path fill="var(--brand-blue)" d="M9 0a9 9 0 0 0-9 9c0 6.5 9 15 9 15s9-8.5 9-15a9 9 0 0 0-9-9zm0 13a4 4 0 1 1 0-8 4 4 0 0 1 0 8z"/></svg>
      87 Harrowgate Ave, Pindarra, QLD, 4000
    </p>
  </section>

  <section class="card card-back" aria-label="Business card back">
    <p class="back-wordmark">QUENDIX</p>
  </section>
</main>
</body>
</html>
```